buseisness card

design a card that similar to my web site
BRIXENTAPLORLLC .COM

Contact Information for Business Card

NAME PHONE # WEBSITE EMAIL AND DISCTIPTION OF WHAT WE DO

Colors
0054AA
0677BA
7BADD7
CADEEF
E8F1F8

Requirements
Must have
• lOGO AND DETAILS
Nice to have
• I LIKE THE WATER LIKE ON MY WEB SITE

```html
<!DOCTYPE html>
<html lang="en">
<head>
<meta charset="utf-8">
<title>Brixentaplor Business Card</title>
<link href="https://fonts.googleapis.com/css2?family=Montserrat:wght@700&family=Poppins:wght@500;600&family=Roboto:ital,wght@0,400;0,500;0,700;1,500&display=swap" rel="stylesheet">
<style>
  :root {
    --page-bg: #e9e6e1;
    --card-dark: #1f1f20;
    --brand-blue: #2a86c4;
    --deep-blue: #0054aa;
    --mid-blue: #0677ba;
    --light-blue: #7badd7;
    --text-white: #ffffff;
  }
  * { margin: 0; padding: 0; box-sizing: border-box; }
  html, body {
    width: 900px; height: 1200px; overflow: hidden;
    background: var(--page-bg);
  }
  .canvas { position: relative; width: 900px; height: 1200px; }
  .card {
    position: absolute; border-radius: 22px; overflow: hidden;
    box-shadow: 0 6px 18px rgba(0,0,0,0.25);
  }
  /* Front card */
  .card-front {
    left: 72px; top: 135px; width: 773px; height: 448px;
    background: var(--card-dark); color: var(--text-white);
    font-family: "Roboto", sans-serif;
  }
  .person-name {
    position: absolute; left: 46px; top: 68px;
    font-family: "Poppins", sans-serif; font-weight: 600;
    font-size: 28px; letter-spacing: 1.6px; color: var(--brand-blue);
  }
  .person-title {
    position: absolute; left: 46px; top: 101px;
    font-family: "Poppins", sans-serif; font-weight: 600;
    font-size: 22px; letter-spacing: 2px;
  }
  .contact-list { position: absolute; left: 46px; top: 200px; list-style: none; }
  .contact-item {
    display: flex; align-items: center; gap: 9px;
    font-size: 20px; letter-spacing: 0.4px; height: 31.5px;
  }
  .contact-icon { width: 25px; height: 22px; flex: none; }
  .address {
    position: absolute; left: 44px; top: 352px;
    font-size: 20px; line-height: 27px; letter-spacing: 0.2px;
  }
  .brand-mark {
    position: absolute; left: 500px; top: 80px; width: 210px;
    display: flex; flex-direction: column; align-items: center; gap: 22px;
  }
  .brand-dot {
    width: 120px; height: 120px; border-radius: 50%;
    background: var(--brand-blue);
  }
  .brand-name-front {
    font-family: "Poppins", sans-serif; font-weight: 600;
    font-size: 26px; letter-spacing: 1px; color: var(--brand-blue);
  }
  .services {
    position: absolute; right: 43px; top: 360px; text-align: right;
    font-weight: 700; font-size: 16.5px; line-height: 24px;
  }
  .services .service-sub { font-weight: 500; }
  /* Back card */
  .card-back {
    left: 74px; top: 624px; width: 774px; height: 449px;
    color: var(--text-white); font-family: "Roboto", sans-serif;
  }
  .water-backdrop {
    position: absolute; inset: 0;
    background:
      radial-gradient(ellipse at 80% 30%, rgba(123,173,215,0.45), transparent 55%),
      linear-gradient(135deg, #1d4f78 0%, #1f6492 45%, #2a80b3 75%, #1d5f8c 100%);
  }
  .back-content {
    position: absolute; inset: 0;
    display: flex; flex-direction: column; align-items: center;
  }
  .brand-dot-back {
    margin-top: 80px; width: 150px; height: 150px; border-radius: 50%;
    background: var(--text-white);
  }
  .brand-name-back {
    margin-top: 48px;
    font-family: "Montserrat", sans-serif; font-weight: 700;
    font-size: 52px; letter-spacing: 0.5px; line-height: 1;
  }
  .tagline {
    margin-top: 14px; font-style: italic; font-weight: 500; font-size: 20px;
  }
</style>
</head>
<body>
<main class="canvas">
  <section class="card card-front">
    <h1 class="person-name">MARLOW KEENE</h1>
    <p class="person-title">DIRECTOR</p>
    <ul class="contact-list">
      <li class="contact-item">
        <svg class="contact-icon" viewBox="0 0 25 22" aria-hidden="true">
          <rect x="1" y="4" width="23" height="15" rx="1.5" fill="#2a86c4"/>
          <path d="M1.5 5 L12.5 13 L23.5 5" fill="none" stroke="#1f1f20" stroke-width="1.6"/>
        </svg>
        +740 555 0182
      </li>
      <li class="contact-item">
        <svg class="contact-icon" viewBox="0 0 25 22" aria-hidden="true">
          <path d="M2 8 Q12.5 1 23 8 L21 11 L17 9.5 L17 7.5 Q12.5 6 8 7.5 L8 9.5 L4 11 Z" fill="#2a86c4"/>
          <path d="M6 12 L9 9 L16 9 L19 12 L20 19 L5 19 Z" fill="#2a86c4"/>
          <circle cx="12.5" cy="14" r="2.4" fill="#1f1f20"/>
        </svg>
        mk@bx208.com
      </li>
      <li class="contact-item">
        <svg class="contact-icon" viewBox="0 0 25 22" aria-hidden="true">
          <g fill="none" stroke="#2a86c4" stroke-width="1.7">
            <circle cx="12.5" cy="11" r="9.5"/>
            <ellipse cx="12.5" cy="11" rx="4.2" ry="9.5"/>
            <line x1="3" y1="11" x2="22" y2="11"/>
            <path d="M4.5 6 H20.5 M4.5 16 H20.5"/>
          </g>
        </svg>
        brixentaplorllc.com
      </li>
    </ul>
    <p class="address">4318 Harborline, Parkway<br>Westerly, OH 43990</p>
    <div class="brand-mark">
      <span class="brand-dot" aria-hidden="true"></span>
      <span class="brand-name-front">BRIXENTAPLOR</span>
    </div>
    <p class="services">FOAM PROPORTIONER TESTING<br><span class="service-sub">HEF, AR, And AFFF Systems</span></p>
  </section>

  <section class="card card-back">
    <div class="water-backdrop" role="img" aria-label="Underwater photograph of deep blue water with rising bubbles"></div>
    <div class="back-content">
      <span class="brand-dot-back" aria-hidden="true"></span>
      <h2 class="brand-name-back">BRIXENTAPLOR</h2>
      <p class="tagline">An Eco Friendly Company Doing Eco Friendly Testing</p>
    </div>
  </section>
</main>
</body>
</html>
```